Valdur Net Defence (Consultants)

We need a webdesign for a new website www.valdurnetdefence.com.

A draft version of the website is online. You can also look at our linkedIn company page: http://www.brelvo.com/company/7719406

This is what we do:
We defend our cybersociety against the growing number of cyber threats in order to allow our society to prosper and evolve more safely into the digital age. We seek to protect 4 key pillars of our society: critical (industrial) infrastructures, medical systems, our intellectual property, and financial systems.

Valdur is specialised in IT & information security consultancy and positions itself as an independent partner. Our employees possess a unique mix of technical hands-on engineering and consulting skills. We invest time and resources to learn about existing open-source and commercial technologies in order to give better advice.

We are no-nonsense, practical and to the point.

We advise and guide organisations with the strategy, definition and technical implementation of security projects. We take ownership in aligning the existing business, operational and technical context.

Some requirements:
- Ideally you deliver a fully coded and designed static website. I am hosting the website on www.hostplume.com; you can use the technologies that are supported there.
- My existing company colors and logos need to be preserved (see existing websites & linkedIn page)
- I would like a white background (is the best fit for my existing logo's, and easiest to maintain afterwards)
Some examples, but please feel free: http://www.gravelock.com/ http://www.mervion.com/ )
- I will use twitter as a way to update my website with relevant news ; So I want the twitterfeed integrated in the website, certianly on the homepage; if possible on all pages. (www.chirpwall.com/valdurdefence)
- I am using my linkedIn company page; I want at least the "Follow" company button to be integrated in the website. (http://www.brelvo.com/company/valdur-netdefence-consultants/)
- it should be possible for me to do some minor updates to the site.
- I need several nice banners that I could also re-use at my linkedIn webpage (linkedIn requires 646 x 220 pixels or larger banners)

- As I see it now, the website should have a Home page that immediately displays the core services we offer. A basic Jobs page. an about and contact page where people can leave their details behind.
- Optional: An industries tab where there are sub-sites possible
Updates

This project has just been garantueed! First and second place get a nice payment. Please send you designs. 

I need
- A ready to deploy basic HTML webpage
- 4 pages: Home, Services, Careers, About/contact
- Some nice banners designed on my mission statement (in the brief)

Thanks

Reason: We would like to receive some more designs from other designers.

Target Market(s)

From medium sized KMO's, to mainly big enterprises.
My focusses is on strategic consulting, So managers, decision takers & business people
The site should also attrack consultants that have technical skills and managerial skills...

Industry/Entity Type

Financial

Requirements
Must have
• - My existing company colors and logos need to be preserved (see existing websites & linkedIn page)
- I would like a clean, professional site, with a white background
- As I see it now, the website should have a Home page that immediately displays the core services we offer. A basic careers page. an about and contact page where people can leave their details behind.
Nice to have
• - it should be possible for me to do some minor updates to the site.

```html
<!DOCTYPE html>
<html lang="en">
<head>
<meta charset="utf-8">
<title>Valdur Net Defence</title>
<link href="https://fonts.googleapis.com/css2?family=Open+Sans:wght@400;600;700&family=Arimo:wght@400;700&display=swap" rel="stylesheet">
<style>
:root{
  --red:#c0001f;
  --red-dark:#a3001a;
  --ink:#333;
  --body:#555;
  --line:#ddd;
  --footer:#222;
  --white:#fff;
}
*{margin:0;padding:0;box-sizing:border-box}
html,body{width:999px;height:1200px;overflow:hidden;background:var(--white)}
body{position:relative;font-family:Arimo,Arial,sans-serif;color:var(--body)}
.abs{position:absolute}

/* header */
.site-header{left:0;top:0;width:999px;height:72px;background:var(--white)}
.brand{left:202px;top:18px}
.brand-name{font-family:"Open Sans",sans-serif;font-size:24px;font-weight:400;color:var(--ink);letter-spacing:.5px}
.main-nav a{position:absolute;top:0;height:72px;line-height:80px;font-size:9.5px;color:#333;text-decoration:none;text-align:center}
.main-nav a.active{color:var(--red);border-bottom:3px solid var(--red);box-shadow:0 0 6px rgba(0,0,0,.08);background:#fff}

/* hero */
.hero{left:0;top:72px;width:999px;height:318px;background:linear-gradient(90deg,#e9e3dc 0%,#d9d4cf 25%,#f1eeea 45%,#c9b9ac 60%,#efece8 78%,#e6e1da 100%)}
.hero-caption{left:200px;top:190px;width:340px;height:104px;background:rgba(30,30,30,.82);padding:17px 16px;font-family:"Open Sans",sans-serif;font-weight:700;font-size:12.4px;line-height:22px;color:#fff;text-transform:uppercase;white-space:nowrap}
.hero-caption .fold{position:absolute;right:0;top:0;width:0;height:0;border-top:20px solid var(--red);border-left:20px solid transparent}

/* services */
.service{width:300px}
.service-icon{position:absolute;left:0;top:0;width:61px;height:61px}
.service h2{position:absolute;left:70px;top:0;font-family:"Open Sans",sans-serif;font-size:14.5px;font-weight:700;color:#444;white-space:nowrap}
.service p{position:absolute;left:70px;top:26px;font-size:8.6px;line-height:11.2px;color:#555;white-space:nowrap}

/* social band */
.social-band{left:0;top:660px;width:999px;height:202px;background:var(--red)}
.band-notch-top{left:490px;top:660px;width:0;height:0;border-left:10px solid transparent;border-right:10px solid transparent;border-top:10px solid var(--white)}
.band-notch-bottom{left:490px;top:862px;width:0;height:0;border-left:10px solid transparent;border-right:10px solid transparent;border-top:10px solid var(--red)}
.band-lead{left:266px;top:678px;font-size:11.6px;line-height:19px;color:#fff;white-space:nowrap}
.follow-btn{display:inline-flex;align-items:center;gap:3px;background:#fff;border:1px solid #ccc;border-radius:2px;padding:0 4px;height:12px;font-size:7.5px;color:#333;vertical-align:middle;margin-left:6px}
.follow-btn i{display:inline-block;width:7px;height:7px;background:#1f6fa8}
.feed-badge{width:34px;height:34px;border:2px solid #fff;border-radius:50%}
.feed-badge::after{content:"";position:absolute;left:10px;top:10px;width:10px;height:10px;background:#fff;border-radius:50%}
.tweet{width:197px;height:82px;background:#fff;border-radius:2px;padding:9px 11px;font-size:8.2px;line-height:11.4px;color:#444;white-space:nowrap}
.tweet::before{content:"";position:absolute;left:-7px;top:22px;border-top:7px solid transparent;border-bottom:7px solid transparent;border-right:7px solid #fff}
.tweet .handle{margin-bottom:6px}
.tweet a{color:var(--red);text-decoration:none}

/* contact */
.contact-title{left:0;top:884px;width:999px;text-align:center;font-family:"Open Sans",sans-serif;font-size:22.5px;font-weight:700;color:var(--red)}
.contact-panel{left:200px;top:925px;width:600px;height:164px;border:1px solid #ccc;border-radius:2px;background:linear-gradient(180deg,#f3f3f3,#e9e9e9);box-shadow:0 1px 3px rgba(0,0,0,.15)}
.panel-title{left:0;top:23px;width:100%;text-align:center;font-size:16px;font-weight:400;color:#333}
.panel-sub{left:0;top:44px;width:100%;text-align:center;font-size:8.5px;color:#555}
.panel-rule{left:21px;top:65px;width:558px;height:1px;background:var(--line)}
.field{top:84px;height:22px;background:#fff;border:1px solid #ccc;border-radius:2px;padding:0 8px;font-size:7.4px;line-height:20px;color:#aaa;font-style:italic;white-space:nowrap;overflow:hidden}
.submit{left:514px;top:84px;width:63px;height:22px;background:linear-gradient(180deg,#d5112f,var(--red-dark));color:#fff;font-family:"Open Sans",sans-serif;font-weight:700;font-size:10.5px;text-align:center;line-height:22px;border-radius:2px}
.contact-item{top:116px;display:flex;gap:7px;font-size:8.3px;line-height:11px;color:#444}
.contact-item svg{flex:none;margin-top:1px}

/* footer */
.site-footer{left:0;top:1138px;width:999px;height:62px;background:var(--footer)}
.to-top{left:481px;top:1120px;width:38px;height:38px;border-radius:50%;background:var(--footer)}
.copyright{left:578px;top:1166px;font-size:8.2px;color:#fff}
</style>
</head>
<body>

<header class="site-header abs">
  <div class="brand abs"><span class="brand-name">Valdur</span></div>
  <nav class="main-nav">
    <a class="active" style="left:475px;width:58px">Home</a>
    <a style="left:550px;width:48px">Services</a>
    <a style="left:623px;width:48px">Careers</a>
    <a style="left:692px;width:44px">About</a>
    <a style="left:760px;width:44px">Contact</a>
  </nav>
</header>

<section class="hero abs" role="img" aria-label="Photo of a smiling businesswoman in front of colleagues in a bright office"></section>
<div class="hero-caption abs">We advise and guide organisations with<br>the strategy, definition and technical<br>implementation of security projects.<span class="fold"></span></div>

<section class="services">
  <article class="service abs" style="left:200px;top:429px">
    <svg class="service-icon" viewBox="0 0 61 61"><circle cx="30.5" cy="30.5" r="29" fill="none" stroke="#c0001f" stroke-width="2.5"/><path d="M17 26h6l14-7v23l-14-7h-6z" fill="#c0001f"/><rect x="21" y="35" width="4" height="7" fill="#c0001f"/><rect x="39" y="27" width="4" height="7" fill="#c0001f"/></svg>
    <h2>CRITICAL INFRASTRUCTURES</h2>
    <p>Lorem ipsum dolor sit amet, consectetur adipiscing elit.<br>Quisque felis enim, pellentesque vitae suscipit eu, fermen-<br>tum in neque. Maecenas vel orci a lorem tincidunt tempus<br>nec sed dolor. Etiam porttitor accumsan pellentesque.<br>Quisque sapien felis, consequat at rutrum eget, euismod</p>
  </article>
  <article class="service abs" style="left:516px;top:429px">
    <svg class="service-icon" viewBox="0 0 61 61"><circle cx="30.5" cy="30.5" r="29" fill="none" stroke="#c0001f" stroke-width="2.5"/><path d="M26 17h9M28 17v11l-9 15h23l-9-15V17" fill="none" stroke="#c0001f" stroke-width="2"/><path d="M22 38h17l3 5H19z" fill="#c0001f"/></svg>
    <h2>MEDICAL SYSTEMS</h2>
    <p>Lorem ipsum dolor sit amet, consectetur adipiscing elit.<br>Quisque felis enim, pellentesque vitae suscipit eu, fermen-<br>tum in neque. Maecenas vel orci a lorem tincidunt tempus<br>nec sed dolor. Etiam porttitor accumsan pellentesque.<br>Quisque sapien felis, consequat at rutrum eget, euismod</p>
  </article>
  <article class="service abs" style="left:200px;top:541px">
    <svg class="service-icon" viewBox="0 0 61 61"><circle cx="30.5" cy="30.5" r="29" fill="none" stroke="#c0001f" stroke-width="2.5"/><path d="M27 17h7l-2 5h-3z" fill="#c0001f"/><path d="M29 23h3l5 15-6 6-6-6z" fill="#c0001f"/></svg>
    <h2>INTELLECTUAL PROPERTY</h2>
    <p>Lorem ipsum dolor sit amet, consectetur adipiscing elit.<br>Quisque felis enim, pellentesque vitae suscipit eu, fermen-<br>tum in neque. Maecenas vel orci a lorem tincidunt tempus<br>nec sed dolor. Etiam porttitor accumsan pellentesque.<br>Quisque sapien felis, consequat at rutrum eget, euismod</p>
  </article>
  <article class="service abs" style="left:516px;top:541px">
    <svg class="service-icon" viewBox="0 0 61 61"><circle cx="30.5" cy="30.5" r="29" fill="none" stroke="#c0001f" stroke-width="2.5"/><path d="M17 18v26h28" fill="none" stroke="#c0001f" stroke-width="2"/><rect x="21" y="34" width="4" height="8" fill="#c0001f"/><rect x="27" y="30" width="4" height="12" fill="#c0001f"/><rect x="33" y="32" width="4" height="10" fill="#c0001f"/><rect x="39" y="26" width="4" height="16" fill="#c0001f"/><path d="M20 30l8-7 5 4 9-9" fill="none" stroke="#c0001f" stroke-width="2"/><path d="M38 17h5v5z" fill="#c0001f"/></svg>
    <h2>FINANCIAL SYSTEMS</h2>
    <p>Lorem ipsum dolor sit amet, consectetur adipiscing elit.<br>Quisque felis enim, pellentesque vitae suscipit eu, fermen-<br>tum in neque. Maecenas vel orci a lorem tincidunt tempus<br>nec sed dolor. Etiam porttitor accumsan pellentesque.<br>Quisque sapien felis, consequat at rutrum eget, euismod</p>
  </article>
</section>

<section class="social-band abs"></section>
<div class="band-notch-top abs"></div>
<div class="band-notch-bottom abs"></div>
<p class="band-lead abs">Quisque sed orci a nunc vehicula dapibus nec ac augue. Aliquam iaculis tristique diam,<br>vel facilisis velit volutpat et. Aenean at leo sit amet purus <span class="follow-btn"><i></i>Follow</span></p>

<span class="feed-badge abs" style="left:223px;top:760px"></span>
<div class="tweet abs" style="left:268px;top:739px">
  <p class="handle">Valdur Net Defence`@valdurdefence</p>
  <p>Cybersecurity in business term: Positioned<br>by Harlowe's at 3rd place on the global CEO<br>top risks agenda. http://brv.io/hPrpMs<br><a>Details +</a></p>
</div>
<span class="feed-badge abs" style="left:530px;top:760px"></span>
<div class="tweet abs" style="left:575px;top:739px">
  <p class="handle">Valdur Net Defence`@valdurdefence</p>
  <p>Cybersecurity in business term: Positioned<br>by Harlowe's at 3rd place on the global CEO<br>top risks agenda. http://brv.io/hPrpMs<br><a>Details +</a></p>
</div>

<h2 class="contact-title abs">FELL FREE TO COMMUNICATE</h2>
<section class="contact-panel abs" aria-label="Contact form">
  <h3 class="panel-title abs">Fill out the form below to get started</h3>
  <p class="panel-sub abs">volutpat ac molestie non, auctor eu dui libero elementum odio, pretium viverra orci dui eu elit</p>
  <div class="panel-rule abs"></div>
  <div class="field abs" style="left:21px;width:134px">Type your full name</div>
  <div class="field abs" style="left:162px;width:134px">Type your email addres</div>
  <div class="field abs" style="left:304px;width:203px">Tell us a bit about how we couls help you ...</div>
  <div class="submit abs">SUBMIT</div>
  <div class="contact-item abs" style="left:21px">
    <svg width="9" height="12" viewBox="0 0 9 12"><path d="M4.5 0A4.5 4.5 0 0 0 0 4.5C0 8 4.5 12 4.5 12S9 8 9 4.5A4.5 4.5 0 0 0 4.5 0z" fill="#c0001f"/><circle cx="4.5" cy="4.5" r="1.7" fill="#fff"/></svg>
    <span>Marlow House Fenwick Place<br>St Aldens Road</span>
  </div>
  <div class="contact-item abs" style="left:164px">
    <svg width="11" height="11" viewBox="0 0 11 11"><path d="M2 0l2 3-1 1.5c.8 1.5 2 2.7 3.5 3.5L8 7l3 2-1.5 2C5 11 0 6 0 1.5z" fill="#c0001f"/></svg>
    <span>123 - 4567 - 8900</span>
  </div>
  <div class="contact-item abs" style="left:304px">
    <svg width="12" height="9" viewBox="0 0 12 9"><rect width="12" height="9" fill="#c0001f"/><path d="M0 0l6 5 6-5" fill="none" stroke="#fff" stroke-width="1"/></svg>
    <span>info@valdurnetdefence.com</span>
  </div>
</section>

<footer class="site-footer abs"></footer>
<div class="to-top abs"><svg width="38" height="38" viewBox="0 0 38 38"><path d="M13 21l6-6 6 6" fill="none" stroke="#fff" stroke-width="3"/></svg></div>
<p class="copyright abs">Copyright © 2013. Valdur Net Defence. All Rights Reserved.</p>

</body>
</html>
```